We currently have a good logo and we want business cards that can display our logo but also represent our industry - telecom construction - We are a construction company specializing in telecom construction such as installation of fiber optic cable throughout cities and across the country. Nationwide services
We are large enough to handle most any project yet small enough to be a flexible partner and resource.

Target Market(s)

U.S. based telecom carriers and providers

Industry/Entity Type

Construction

Contact Information for Business Card

Business cards should include our logo, phone number and website address. Also, including some information as to our core services would be good.

Colors

Designer to choose colors to be used in the design.

Requirements
Must have
• Colors based on logo
• Must use our logo
• Logo, name, email, website address, phone number
• Tovasco Conduit
• Brent Halvik
• Director of Business Development
• (555) 271-0386
• www.TVSQ-example.com
Nice to have
• Construction services including:
• Small Cell Construction
• Boring/Drilling
• Plowing / Trenching
• Conduit installation
• Fiber pulling
• splicing
• building entries
• Aerial construction
• Aerial Make Ready
• Make Ready Engineering
Should not have
• We are open to ideas

```html
<!DOCTYPE html>
<html lang="en">
<head>
<meta charset="utf-8">
<title>Tovasco Conduit – Business Card</title>
<link href="https://fonts.googleapis.com/css2?family=Arimo:wght@400;700&display=swap" rel="stylesheet">
<style>
  :root {
    --backdrop: #2b2b2d;
    --card: #0d0d0e;
    --card-edge: #1a1a1c;
    --brand-blue: #1a9be6;
    --brand-blue-deep: #0d6fc0;
    --text-light: #f2f2f2;
    --text-muted: #b9bcc0;
    --rule: #55585c;
  }
  * { margin: 0; padding: 0; box-sizing: border-box; }
  html, body {
    width: 1200px;
    height: 900px;
    overflow: hidden;
    background: var(--backdrop);
    font-family: "Arimo", Arial, sans-serif;
  }
  .sheet {
    position: relative;
    width: 1200px;
    height: 900px;
    display: flex;
    flex-direction: column;
    align-items: center;
    justify-content: center;
    gap: 40px;
  }
  .card {
    position: relative;
    width: 560px;
    height: 320px;
    background: linear-gradient(160deg, var(--card-edge) 0%, var(--card) 55%);
    box-shadow: 0 14px 30px rgba(0,0,0,0.45);
    overflow: hidden;
  }
  .card__band {
    position: absolute;
    left: 0;
    right: 0;
    bottom: 8px;
    height: 8px;
    background: var(--brand-blue);
  }
  /* Front */
  .card--front {
    display: flex;
    align-items: center;
    justify-content: center;
  }
  .brand {
    display: flex;
    align-items: center;
    gap: 12px;
    margin-bottom: 24px;
  }
  .brand__mark {
    width: 18px;
    height: 18px;
    background: var(--brand-blue);
  }
  .brand__name {
    font-weight: 700;
    font-size: 38px;
    letter-spacing: 0.5px;
    color: var(--brand-blue);
  }
  /* Back */
  .card--back {
    display: flex;
    flex-direction: column;
    align-items: center;
    padding-top: 36px;
    text-align: center;
  }
  .contact__name {
    font-weight: 700;
    font-size: 17px;
    letter-spacing: 0.5px;
    color: var(--brand-blue);
    text-transform: uppercase;
  }
  .contact__title {
    font-size: 13px;
    color: var(--text-light);
    margin-top: 2px;
  }
  .contact__icons {
    display: flex;
    align-items: center;
    gap: 5px;
    margin-top: 8px;
  }
  .contact__icons .rule {
    width: 44px;
    height: 1px;
    background: var(--rule);
    margin: 0 6px;
  }
  .icon {
    width: 20px;
    height: 20px;
    border-radius: 4px;
    background: var(--brand-blue);
    display: flex;
    align-items: center;
    justify-content: center;
  }
  .icon svg { width: 13px; height: 13px; }
  .contact__lines {
    margin-top: 8px;
    font-size: 13px;
    line-height: 17px;
    color: var(--text-light);
  }
  .divider {
    width: 140px;
    height: 1px;
    background: var(--rule);
    margin: 8px 0 6px;
  }
  .services {
    font-size: 13px;
    line-height: 17px;
    color: var(--text-light);
  }
  .services .sep { color: var(--brand-blue); padding: 0 3px; }
</style>
</head>
<body>
  <main class="sheet">
    <section class="card card--front" aria-label="Card front">
      <div class="brand">
        <span class="brand__mark"></span>
        <span class="brand__name">Tovasco Conduit</span>
      </div>
      <div class="card__band"></div>
    </section>

    <section class="card card--back" aria-label="Card back">
      <h1 class="contact__name">Brent Halvik</h1>
      <p class="contact__title">Director of Business Development</p>
      <div class="contact__icons">
        <span class="rule"></span>
        <span class="icon" aria-label="Phone">
          <svg viewBox="0 0 24 24"><path fill="#0d0d0e" d="M6.6 10.8a15.2 15.2 0 0 0 6.6 6.6l2.2-2.2c.3-.3.7-.4 1-.2 1.1.4 2.3.6 3.6.6.6 0 1 .4 1 1V20c0 .6-.4 1-1 1A17 17 0 0 1 3 4c0-.6.4-1 1-1h3.5c.6 0 1 .4 1 1 0 1.3.2 2.5.6 3.6.1.3 0 .7-.2 1z"/></svg>
        </span>
        <span class="icon" aria-label="Email">
          <svg viewBox="0 0 24 24"><path fill="#0d0d0e" d="M3 5h18v14H3zm2 2v.5l7 4.5 7-4.5V7zm0 2.9V17h14V9.9l-7 4.5z"/></svg>
        </span>
        <span class="icon" aria-label="Website">
          <svg viewBox="0 0 24 24"><circle cx="12" cy="12" r="8.5" fill="none" stroke="#0d0d0e" stroke-width="2"/><path d="M3.5 12h17M12 3.5c3 3 3 14 0 17M12 3.5c-3 3-3 14 0 17" fill="none" stroke="#0d0d0e" stroke-width="1.6"/></svg>
        </span>
        <span class="rule"></span>
      </div>
      <div class="contact__lines">
        <p>(555) 271-0386</p>
        <p>info@tvsq-example.com</p>
        <p>www.TVSQ-example.com</p>
      </div>
      <div class="divider"></div>
      <div class="services">
        <p>Small Cell Construction<span class="sep">|</span>Boring/Drilling<span class="sep">|</span>Plowing / Trenching</p>
        <p>Conduit installation<span class="sep">|</span>Fiber pulling<span class="sep">|</span>splicing</p>
        <p>building entries<span class="sep">|</span>Aerial construction<span class="sep">|</span>Aerial Make Ready</p>
        <p>Make Ready Engineering</p>
      </div>
      <div class="card__band"></div>
    </section>
  </main>
</body>
</html>
```